Need a graphic design for front page of tech blog

Hi,

So I'm looking to start a project of redesigning the front homepage for all of my tech sites. I already have a developer that will code the change, so what I need from someone here is to give me a graphic design, which I can then give to my developers to code.

Currently, I have the plain old boring default list of WordPress posts as the front page, which needs to be replaced with something a little more like a magazine or newspaper style. You can see my four sites here:

https://www.quill-gadget-notes.com/
https://servicebenchnerd.com/
https://theatticbitworks.com/
https://www.hoppingtolark.com/

I've attached some screenshots of mobile sites that I like in terms of look and style. Some desktop sites that I like are here (I like some parts more than others, I've attached screenshots of the sections I like):

https://www.ploddernook.com/
https://www.gizmonest.com/
https://www.pinewirebulletin.com/
https://www.takeholdwith.com/
https://www.dayspool.com/

Basically, I don't need all that text after each post. Seems like most sites now just have an image, a title, the author and date info and possibly the category.

Right now I'm only showing 10 posts and one has to scroll through lots of text to see them all. The sidebar is good, but I think we can get rid of that for the front page and instead have different sections like Latest Tips, and then some section headers based on the categories.

Anyway, I'm looking for someone who can come up with multiple designs, so that I have some choice.

I'm looking to get this done over the next few weeks. Also, please include in your price the cost of any revisions and how many revisions can be done.

Thanks

Tarun

```html
<!DOCTYPE html>
<html lang="en">
<head>
<meta charset="utf-8">
<title>Quill Gadget Notes – Mobile Home &amp; Search</title>
<link rel="stylesheet" href="https://fonts.googleapis.com/css2?family=Poppins:wght@400;500;600;700&family=Source+Serif+4:wght@400&display=swap">
<style>
:root{
  --bg:#f4f4f6;
  --screen:#ececef;
  --ink:#1b1b1f;
  --muted:#3c4250;
  --orange:#dc560d;
  --tag:#e8601a;
  --white:#ffffff;
  --hero-a:#7a4a35;
  --hero-b:#2a1f22;
}
*{box-sizing:border-box;margin:0;padding:0}
html,body{width:1200px;height:1200px;overflow:hidden;background:var(--bg)}
body{font-family:"Poppins",sans-serif;color:var(--ink);position:relative}
.screen{position:absolute;top:190px;width:380px;height:820px;background:var(--screen);overflow:hidden;border-radius:28px}
.screen--home{left:160px}
.screen--search{left:660px}

/* home */
.site-header{height:74px;display:flex;align-items:center;justify-content:space-between;padding:0 22px}
.site-name{font-weight:700;font-size:13px;letter-spacing:.02em;color:var(--ink);display:flex;align-items:center;gap:7px}
.site-name .dot{width:9px;height:9px;background:var(--orange);border-radius:50%}
.header-icons{display:flex;gap:14px}
.hero{position:relative;height:400px;display:flex}
.hero-card{position:relative;flex:0 0 322px;height:100%;margin-right:6px}
.hero-card--peek{flex:0 0 60px;margin:0}
.photo{position:absolute;inset:0}
.hero-card .photo{background:linear-gradient(160deg,var(--hero-a) 0%,#5a3a32 40%,var(--hero-b) 100%)}
.hero-card--peek .photo{background:linear-gradient(180deg,#4a2f30,#1e1a20)}
.hero-text{position:absolute;left:16px;bottom:36px;right:10px;color:var(--white)}
.tag{display:inline-block;background:var(--tag);color:var(--white);font-size:11px;font-weight:500;padding:4px 12px;line-height:1.2}
.hero-title{font-size:26px;font-weight:600;line-height:1.25;margin:12px 0 14px}
.byline{font-family:"Source Serif 4",serif;font-size:15px}
.byline a{color:var(--orange);text-decoration:none}
.hero-card--peek .hero-text{left:16px;white-space:nowrap}
.posts{display:flex;gap:10px;padding:48px 16px 0}
.post{flex:1;min-width:0}
.post .thumb{position:relative;height:175px}
.post .thumb .photo.pie{background:linear-gradient(150deg,#7b4a2c,#3d3230 60%,#6a6060)}
.post .thumb .photo.note{background:linear-gradient(150deg,#5c6068,#2a2c30 55%,#7b6a5a)}
.post .tag{position:absolute;left:0;bottom:0}
.post-title{font-size:17px;font-weight:500;line-height:1.6;margin-top:14px}
.post .byline{margin-top:10px;font-size:15px}

/* search */
.close{position:absolute;right:22px;top:50px}
.search-field{position:absolute;left:24px;right:24px;top:180px;height:70px;border-bottom:3px solid var(--ink);display:flex;align-items:center;gap:22px;padding-bottom:6px}
.search-field span{font-size:30px;font-weight:600;color:#d2d3d8}
.search-hint{position:absolute;left:24px;top:294px;font-size:18px;color:var(--muted)}
.suggest{position:absolute;left:16px;right:16px;bottom:16px;height:400px;background:var(--orange);border-radius:0 0 24px 24px;color:var(--white);padding:88px 16px 0}
.suggest h2{font-size:21px;font-weight:600;margin-bottom:36px}
.suggest p{font-size:20px;font-weight:600;line-height:1.42;letter-spacing:-.2px;white-space:nowrap}
</style>
</head>
<body>

<section class="screen screen--home" aria-label="Mobile home page">
  <header class="site-header">
    <div class="site-name"><span class="dot"></span>QUILL GADGET NOTES</div>
    <div class="header-icons">
      <svg width="20" height="20" viewBox="0 0 20 20" fill="none" stroke="#1b1b1f" stroke-width="2"><circle cx="8.5" cy="8.5" r="6"/><path d="M13 13l5 5"/></svg>
      <svg width="20" height="20" viewBox="0 0 20 20" stroke="#1b1b1f" stroke-width="2"><path d="M2 4h16M2 10h16M2 16h16"/></svg>
    </div>
  </header>

  <div class="hero">
    <article class="hero-card">
      <div class="photo" role="img" aria-label="Photo of a monitor showing a streaming service library"></div>
      <div class="hero-text">
        <span class="tag">Tips</span>
        <h1 class="hero-title">How To Use StreamBox's Parental Control Feature</h1>
        <p class="byline">By Dario Vell</p>
      </div>
    </article>
    <article class="hero-card hero-card--peek">
      <div class="photo" role="img" aria-label="Photo for the next featured tip"></div>
      <div class="hero-text">
        <span class="tag">Tips</span>
        <h1 class="hero-title">Ho<br>Yo<br>Ho<br>On</h1>
        <p class="byline">By M</p>
      </div>
    </article>
  </div>

  <div class="posts">
    <article class="post">
      <div class="thumb">
        <div class="photo pie" role="img" aria-label="Photo of a slice of pie on a cooling rack"></div>
        <span class="tag">Review</span>
      </div>
      <h2 class="post-title">Tandrel OS Pie (v9) Review – The “Techie”</h2>
    </article>
    <article class="post">
      <div class="thumb">
        <div class="photo note" role="img" aria-label="Photo of a smartphone with a stylus note on its screen"></div>
        <span class="tag">Review</span>
      </div>
      <h2 class="post-title">Orbitek Nova Note 9 Review</h2>
      <p class="byline">By <a href="#">Mira Holt</a></p>
    </article>
  </div>
</section>

<section class="screen screen--search" aria-label="Search overlay">
  <svg class="close" width="20" height="20" viewBox="0 0 20 20" stroke="#1b1b1f" stroke-width="2.6"><path d="M3 3l14 14M17 3L3 17"/></svg>
  <div class="search-field">
    <svg width="36" height="36" viewBox="0 0 36 36" fill="none" stroke="#1b1b1f" stroke-width="3.5"><circle cx="15" cy="15" r="11"/><path d="M23 23l10 10"/></svg>
    <span>Search</span>
  </div>
  <p class="search-hint">Hit enter to search or ESC to close</p>
  <div class="suggest">
    <h2>→ May We Suggest?</h2>
    <p>#drone #funny #catgif<br>#broken #lost #hilarious<br>#good #red #blue #nono<br>#why #yes #yesyes #aliens<br>#green</p>
  </div>
</section>

</body>
</html>
```